Hair Extension Aftercare sheet

This sheet is to give to customers regarding the aftercare of hair extensions. There should be Simple and minimal look - approx A5 size and can be folded to suit. I have attached the content and logo files for use.
We are not looking for to much artwork just clean, professional look.
All the content provided in a compact flyer format i.e
A foldable A5 pamphlet or the like, this is for packaging requirements
Please do not submit A4 layouts

Industry/Entity Type

Hair And Beauty

Requirements
Must have
• All the content provided in a compact flyer format i.e
• A foldable A5 pamphlet or the like, this is for packaging requirements
Should not have
• tacky art work or images - must be clean lines

```html
<!DOCTYPE html>
<html lang="en">
<head>
<meta charset="utf-8">
<title>Maren Holt Hair Extensions – Aftercare Pamphlet</title>
<link href="https://fonts.googleapis.com/css2?family=Old+Standard+TT:wght@400&family=Lato:wght@400;700&family=Oswald:wght@300;400&display=swap" rel="stylesheet">
<style>
  :root {
    --gold: #d4ae4e;
    --gold-bright: #e0a93a;
    --ink: #2b2a28;
    --band: #2e2e2e;
    --paper: #ffffff;
    --stage: #ececec;
    --sky: #3fa6a8;
    --teal-deep: #1f5d63;
    --hair: #a45a2c;
  }
  * { margin: 0; padding: 0; box-sizing: border-box; }
  html, body {
    width: 1029px;
    height: 1200px;
    overflow: hidden;
    background: var(--stage);
  }
  .pamphlet {
    position: absolute;
    left: 24px;
    top: 251px;
    width: 980px;
    height: 697px;
    display: flex;
    box-shadow: 0 4px 14px rgba(0,0,0,0.25);
  }
  .panel {
    position: relative;
    width: 490px;
    height: 697px;
    overflow: hidden;
  }
  .panel-story { background: var(--gold); }
  .panel-cover { background: var(--paper); border-left: 1px solid #ddd; }
  .panel-shapes {
    position: absolute;
    inset: 0;
  }
  .story-text {
    position: absolute;
    left: 20px;
    top: 18px;
    width: 450px;
    font-family: "Lato", sans-serif;
    color: var(--ink);
    font-size: 10.4px;
    line-height: 13.6px;
    text-align: justify;
  }
  .story-text h2 {
    font-family: "Old Standard TT", serif;
    font-weight: 400;
    font-size: 20px;
    line-height: 24px;
    margin-bottom: 4px;
  }
  .story-text p { margin-bottom: 13px; }
  .story-text .narrow { width: 305px; }
  .story-text h2.second { margin-top: 12px; }
  .brand {
    position: absolute;
    text-align: center;
    color: var(--ink);
  }
  .brand-name {
    font-family: "Old Standard TT", serif;
    font-size: 18px;
    letter-spacing: 3px;
    line-height: 20px;
  }
  .brand-sub {
    font-family: "Old Standard TT", serif;
    font-size: 8px;
    letter-spacing: 2.4px;
    line-height: 11px;
  }
  .brand-story { left: 130px; top: 590px; width: 190px; }
  .site-story {
    font-family: "Lato", sans-serif;
    font-size: 14px;
    margin-top: 10px;
  }
  .brand-cover { left: 20px; top: 505px; width: 190px; }
  .cover-headline {
    position: absolute;
    left: 23px;
    top: 565px;
    font-family: "Old Standard TT", serif;
    font-size: 29px;
    line-height: 34px;
    color: var(--ink);
  }
  .cover-tagline {
    position: absolute;
    left: 23px;
    top: 600px;
    font-family: "Oswald", sans-serif;
    font-weight: 300;
    font-size: 28px;
    line-height: 34px;
    color: var(--gold-bright);
  }
  .cover-site {
    position: absolute;
    left: 25px;
    top: 640px;
    font-family: "Lato", sans-serif;
    font-size: 13px;
    letter-spacing: 7.2px;
    color: var(--ink);
  }
</style>
</head>
<body>
<main class="pamphlet">

  <section class="panel panel-story">
    <svg class="panel-shapes" width="490" height="697" viewBox="0 0 490 697">
      <defs>
        <linearGradient id="portraitTone" x1="0" y1="0" x2="0" y2="1">
          <stop offset="0" stop-color="#8a6a4a"/>
          <stop offset="0.45" stop-color="#c9a577"/>
          <stop offset="1" stop-color="#1e1e1e"/>
        </linearGradient>
      </defs>
      <polygon points="0,697 490,205 490,697" fill="var(--band)"/>
      <polygon points="0,690 490,213 490,686 0,686" fill="var(--paper)"/>
      <rect x="0" y="686" width="490" height="11" fill="var(--band)"/>
      <rect x="306" y="392" width="176" height="294" fill="url(#portraitTone)" role="img" aria-label="Photo of the stylist in a black leather jacket"/>
    </svg>

    <div class="story-text">
      <h2>About us</h2>
      <p>Maren Holt has been in the hair extension industry for many years, supplying and fitting the highest quality bespoke hand-tied wefts, using the best sourced hair from around the world. Each of our custom wefts is personally hand-crafted by Maren Holt to match the texture and colour of each client's requirements.</p>
      <p>Originally based and trained in the U.K. this is where Maren gained her outstanding skills and knowledge. Maren's attention to detail and passion for high quality hair extensions has driven her to source the very best human hair from all around the world, hair that looks natural and feels amazing.</p>
      <p>Now based in Melbourne Australia, Maren has set about establishing her business built on the principles of quality, attention to detail and value for money.</p>
      <h2 class="second">Maren's story</h2>
      <p class="narrow">I was never gifted genetically with thick luscious hair, my hair was fine, thin &amp; never grew easily. In 1996 at the age of 16, I started using hair extensions to give me the look and feel good factor I sort, I never looked back.</p>
      <p class="narrow">My obsession with hair extensions grew into a passion and I sort to learn everything I could about hair &amp; how to install it. This took me on a path of sourcing &amp; installing high quality hair extensions. Over many years I learned from some of the best technicians in the UK &amp; Europe &amp; gained an extensive client list</p>
    </div>

    <div class="brand brand-story">
      <div class="brand-name">MAREN HOLT</div>
      <div class="brand-sub">HAIR EXTENSIONS</div>
      <div class="site-story">marenholt.com</div>
    </div>
  </section>

  <section class="panel panel-cover">
    <svg class="panel-shapes" width="490" height="697" viewBox="0 0 490 697">
      <defs>
        <linearGradient id="streetTone" x1="0" y1="0" x2="1" y2="1">
          <stop offset="0" stop-color="#3bb3b5"/>
          <stop offset="0.55" stop-color="#c8c29a"/>
          <stop offset="1" stop-color="#a8b84a"/>
        </linearGradient>
        <linearGradient id="hairTone" x1="0" y1="0" x2="1" y2="1">
          <stop offset="0" stop-color="var(--teal-deep)"/>
          <stop offset="0.6" stop-color="var(--hair)"/>
          <stop offset="1" stop-color="#d08a55"/>
        </linearGradient>
        <linearGradient id="mistTone" x1="0" y1="0" x2="0" y2="1">
          <stop offset="0" stop-color="#c9c9c9"/>
          <stop offset="1" stop-color="#ffffff"/>
        </linearGradient>
      </defs>
      <rect x="0" y="190" width="300" height="330" fill="url(#mistTone)" role="img" aria-label="Faint backdrop of flowing hair"/>
      <polygon points="0,0 490,0 490,217 256,462 0,198" fill="url(#streetTone)" role="img" aria-label="Photo of a woman in sunglasses in front of a classical building"/>
      <polyline points="0,208 256,474 490,228" fill="none" stroke="var(--gold)" stroke-width="7"/>
      <polygon points="490,246 270,474 490,640" fill="url(#hairTone)" role="img" aria-label="Photo of a woman with long wavy auburn hair"/>
      <polyline points="490,238 258,478 490,652" fill="none" stroke="var(--gold)" stroke-width="5"/>
      <rect x="0" y="686" width="490" height="11" fill="var(--band)"/>
    </svg>

    <div class="brand brand-cover">
      <div class="brand-name">MAREN HOLT</div>
      <div class="brand-sub">HAIR EXTENSIONS</div>
    </div>
    <div class="cover-headline">Provide High Quality</div>
    <div class="cover-tagline">long lasting hair Extensions</div>
    <div class="cover-site">www.marenholt.com</div>
  </section>

</main>
</body>
</html>
```